Criação de Apres. Comercial (com dobra) para Construção & Engenharia
A empresa queria:
" A VORTIQ é uma empresa de engenharia que atua no mercado há dez anos. Especializada na execução de análises de flexibilidade e detalhamento de suportes, conta com uma equipe de engenheiros e especialistas com vasta experiência, alguns com mais de 25 anos de atuação na área. Oferece a melhor solução com garantia de qualidade, satisfação e respeito aos seus clientes. "

```html
<!DOCTYPE html>
<html lang="pt-BR">
<head>
<meta charset="utf-8">
<title>VORTIQ – Apresentação Comercial</title>
<link rel="stylesheet" href="https://fonts.googleapis.com/css2?family=Oswald:wght@500;700&family=Open+Sans:wght@400;600;700&display=swap">
<style>
  :root {
    --orange: #f26a1b;
    --orange-dark: #d9540c;
    --ink: #2b2b2b;
    --charcoal: #333538;
    --panel: #3d3f42;
    --paper: #f4f4f4;
    --grey: #d6d7d8;
    --stage: #e6e6e6;
  }
  * { box-sizing: border-box; margin: 0; padding: 0; }
  html, body { width: 1200px; height: 1200px; overflow: hidden; }
  body {
    background: var(--stage);
    font-family: "Open Sans", Arial, sans-serif;
    color: var(--ink);
  }
  .spread {
    position: absolute;
    left: 50px; top: 200px;
    width: 1100px; height: 800px;
    display: flex;
    box-shadow: 0 10px 30px rgba(0,0,0,.18);
  }
  .page { position: relative; width: 550px; height: 800px; overflow: hidden; }
  .stripe {
    position: absolute; left: 0; right: 0; bottom: 0; height: 16px;
    background: var(--orange);
  }

  /* Left page */
  .page--intro {
    background: linear-gradient(180deg, #e9e9ea 0%, var(--paper) 40%, #fff 100%);
  }
  .intro__edge {
    position: absolute; left: 0; top: 60px; width: 14px; height: 180px;
    background: var(--charcoal);
  }
  .brand {
    position: absolute; left: 0; right: 0; top: 44px;
    text-align: center;
  }
  .brand__name {
    font-family: "Oswald", "Arial Narrow", sans-serif;
    font-weight: 700; font-size: 56px; line-height: 1; letter-spacing: 2px; color: var(--ink);
  }
  .intro__text {
    position: absolute; left: 70px; top: 140px; width: 440px;
    font-size: 13px; line-height: 1.6; color: #3a3a3a; text-align: justify;
  }
  .intro__text p + p { margin-top: 10px; }
  .intro__photo {
    position: absolute; left: 30px; top: 340px; width: 300px; height: 200px;
    background: linear-gradient(135deg, #c9ced6 0%, #8fa3bd 45%, #e0b64a 100%);
  }
  .areas__title {
    position: absolute; left: 330px; top: 470px; width: 190px;
    font-family: "Oswald", "Arial Narrow", sans-serif; font-weight: 700;
    font-size: 34px; line-height: 1.05; color: var(--orange);
    text-transform: uppercase; text-align: right;
  }
  .areas {
    position: absolute; left: 30px; right: 30px; top: 590px;
    display: flex; justify-content: space-around; list-style: none;
  }
  .area { width: 150px; display: flex; flex-direction: column; align-items: center; gap: 12px; }
  .area__icon {
    width: 84px; height: 84px; border-radius: 50%;
    border: 4px solid var(--charcoal); background: #fff;
    display: flex; align-items: center; justify-content: center;
  }
  .area__label {
    font-size: 12px; font-weight: 700; text-transform: uppercase;
    color: var(--charcoal); text-align: center; letter-spacing: .5px;
  }

  /* Right page */
  .page--services {
    background: linear-gradient(180deg, #c9cacc 0%, var(--grey) 30%, #e4e5e6 100%);
  }
  .services__band {
    position: absolute; left: 0; right: 0; top: 60px; height: 48px;
    background: var(--charcoal);
  }
  .services__title {
    position: absolute; right: 0; top: 52px; height: 64px; padding: 0 34px 0 50px;
    background: var(--charcoal);
    clip-path: polygon(12% 0, 100% 0, 100% 100%, 0 100%);
    font-family: "Oswald", "Arial Narrow", sans-serif; font-weight: 700;
    font-size: 34px; line-height: 64px; color: var(--orange); text-transform: uppercase;
    border-bottom: 4px solid var(--orange);
  }
  .services__grid {
    position: absolute; left: 28px; right: 28px; top: 140px; bottom: 44px;
    display: grid; grid-template-columns: 1fr 1fr 1fr;
    grid-template-rows: 1.1fr 1fr 1.1fr; gap: 12px;
  }
  .tile { position: relative; border: 3px solid var(--panel); }
  .tile--dark { background: var(--panel); padding: 10px; }
  .tile--dark .tile__media { width: 100%; height: 100%; }
  .tile__media { background: linear-gradient(135deg, #f2f2f2 0%, #b9bec4 100%); }
  .tile__media--blue { background: linear-gradient(135deg, #eef1f4 0%, #6f9ac8 55%, #2f5f9a 100%); }
  .tile__media--pipe { background: linear-gradient(135deg, #e8e8e8 0%, #c3c7cc 55%, #8d939a 100%); }
  .tile__media--green { background: linear-gradient(135deg, #eef0ee 0%, #9bb88a 55%, #c96e3a 100%); }
  .tile--light { background: #fff; padding: 6px; }
  .tile--light .tile__media { width: 100%; height: 100%; }
  .tile--text {
    background: var(--orange); border-color: var(--orange-dark);
    padding: 14px 14px; color: #fff;
  }
  .tile__heading {
    font-family: "Oswald", "Arial Narrow", sans-serif; font-weight: 500;
    font-size: 15px; text-transform: uppercase; letter-spacing: .5px; line-height: 1.2;
    margin-bottom: 8px;
  }
  .tile__body { font-size: 12px; line-height: 1.5; }
  .tile__tag {
    position: absolute; left: 10px; top: 10px; background: rgba(255,255,255,.85);
    font-family: "Oswald", "Arial Narrow", sans-serif; font-weight: 500;
    font-size: 13px; padding: 2px 6px; color: var(--ink); text-transform: uppercase;
  }
</style>
</head>
<body>
  <main class="spread">
    <section class="page page--intro">
      <div class="intro__edge"></div>
      <header class="brand">
        <span class="brand__name">VORTIQ</span>
      </header>
      <div class="intro__text">
        <p>A VORTIQ é uma empresa de engenharia que atua no mercado há dez anos. Especializada na execução de análises de flexibilidade e detalhamento de suportes, conta com uma equipe de engenheiros e especialistas com vasta experiência, alguns com mais de 25 anos de atuação na área.</p>
        <p>Oferece a melhor solução com garantia de qualidade, satisfação e respeito aos seus clientes.</p>
      </div>
      <div class="intro__photo" role="img" aria-label="Fotografia de engenheiros com capacetes amarelos analisando um projeto"></div>
      <h2 class="areas__title">Áreas<br>de atuação</h2>
      <ul class="areas">
        <li class="area">
          <div class="area__icon" role="img" aria-label="Ícone de óleo e gás">
            <svg width="40" height="40" viewBox="0 0 40 40"><path d="M20 4 C28 16 32 22 32 27 A12 12 0 0 1 8 27 C8 22 12 16 20 4Z" fill="var(--charcoal)"/></svg>
          </div>
          <span class="area__label">Óleo &amp; Gás</span>
        </li>
        <li class="area">
          <div class="area__icon" role="img" aria-label="Ícone de papel e celulose">
            <svg width="40" height="40" viewBox="0 0 40 40"><path d="M20 4 L34 32 H6Z" fill="var(--charcoal)"/><rect x="18" y="32" width="4" height="6" fill="var(--charcoal)"/></svg>
          </div>
          <span class="area__label">Papel &amp; Celulose</span>
        </li>
        <li class="area">
          <div class="area__icon" role="img" aria-label="Ícone de energia termoelétrica">
            <svg width="40" height="40" viewBox="0 0 40 40"><path d="M24 3 L10 22 H19 L15 37 L30 16 H21Z" fill="var(--charcoal)"/></svg>
          </div>
          <span class="area__label">Termoelétrica &amp; Açúcar</span>
        </li>
      </ul>
      <div class="stripe"></div>
    </section>

    <section class="page page--services">
      <div class="services__band"></div>
      <h2 class="services__title">Serviços</h2>
      <div class="services__grid">
        <div class="tile tile--dark"><div class="tile__media" role="img" aria-label="Modelo 3D de tubulação industrial"></div></div>
        <div class="tile tile--text">
          <h3 class="tile__heading">Análise de flexibilidade</h3>
          <p class="tile__body">Estudos de tensões em tubulações conforme normas ASME.</p>
        </div>
        <div class="tile tile--text">
          <h3 class="tile__heading">Detalhamento de suportes</h3>
          <p class="tile__body">Projeto e detalhamento completo de suportes especiais.</p>
        </div>
        <div class="tile tile--light"><div class="tile__media tile__media--blue" role="img" aria-label="Renderização de conexões de tubulação em azul"></div></div>
        <div class="tile tile--dark"><div class="tile__media" role="img" aria-label="Desenho técnico de estrutura de suporte"></div></div>
        <div class="tile tile--light"><div class="tile__media tile__media--pipe" role="img" aria-label="Vista de linhas de tubulação em planta"></div></div>
        <div class="tile tile--light"><div class="tile__media tile__media--pipe" role="img" aria-label="Curva de tubulação em aço"></div></div>
        <div class="tile tile--text">
          <h3 class="tile__heading">Modelagem 3D</h3>
          <p class="tile__body">Modelos de tubulação integrados ao projeto da planta.</p>
        </div>
        <div class="tile tile--light">
          <div class="tile__media tile__media--green" role="img" aria-label="Modelo de análise sísmica de tubulação"></div>
          <span class="tile__tag">Análise sísmica</span>
        </div>
      </div>
      <div class="stripe"></div>
    </section>
  </main>
</body>
</html>
```